Cedar Hollow Candle Banner Ad for Upcoming holidays

We would like for you to design an ad for Memorial day and Father's Day. For Memorial Day the sale will be 25% OFF select candles and free shipping when you order $50 or more.
For father's day the deal will be get 30% off all candles and free shipping when you order $75 or more.
Please note: These banners will be on our website, they do not require our logo.Banner size: 314 height x 783 width

Industry/Entity Type

Shipping

Requirements
Must have
• Banner size: 314 height x 783 width
Nice to have
• Picture of our starlit candle
Should not have
• Logo

```html
<!DOCTYPE html>
<html lang="en">
<head>
<meta charset="utf-8">
<title>Cedar Hollow Candle – Father's Day Deal</title>
<link href="https://fonts.googleapis.com/css2?family=Parisienne&family=Questrial&family=Oswald:wght@700&family=Arimo:wght@700&display=swap" rel="stylesheet">
<style>
  :root {
    --brown: #6b5a44;
    --teal: #5f8b7d;
    --cream: #f8f6e5;
    --ivory: #f3ead2;
    --white: #ffffff;
    --red: #c01f2f;
    --text-teal: #5a8a78;
    --text-brown: #6b5a44;
  }
  * { margin: 0; padding: 0; box-sizing: border-box; }
  html, body { width: 1200px; height: 481px; overflow: hidden; background: var(--cream); }
  .banner { position: relative; width: 1200px; height: 481px; background: var(--cream); overflow: hidden; }
  .top-band { position: absolute; left: 0; top: 0; width: 1200px; height: 82px; }
  .bottom-band { position: absolute; left: 0; bottom: 0; width: 1200px; height: 16px; background: var(--brown); }
  .badge { position: absolute; left: 22px; top: 128px; width: 326px; height: 326px; }
  .badge-title {
    position: absolute; left: 22px; top: 128px; width: 326px; height: 326px;
    display: flex; flex-direction: column; align-items: center; justify-content: center;
    font-family: 'Oswald', sans-serif; font-weight: 700; color: var(--ivory);
    text-transform: uppercase; line-height: 0.95; text-align: center;
  }
  .badge-title .small { font-size: 31px; letter-spacing: 0.5px; }
  .badge-title .large { font-size: 76px; letter-spacing: 1px; }
  .headline {
    position: absolute; left: 468px; top: 112px;
    font-family: 'Parisienne', cursive; font-size: 38px; color: var(--text-brown);
  }
  .lede {
    position: absolute; left: 412px; top: 166px; width: 440px;
    font-family: 'Questrial', sans-serif; font-size: 21px; line-height: 1.28; color: var(--text-teal);
  }
  .save { position: absolute; left: 512px; top: 234px; font-family: 'Questrial', sans-serif; font-size: 27px; color: var(--text-teal); }
  .discount {
    position: absolute; left: 514px; top: 258px;
    font-family: 'Arimo', sans-serif; font-weight: 700; color: var(--red);
    font-size: 118px; line-height: 1; letter-spacing: -2px;
  }
  .discount sup { font-size: 56px; vertical-align: 44px; margin-left: 4px; }
  .scope { position: absolute; left: 512px; top: 384px; font-family: 'Questrial', sans-serif; font-size: 25px; color: var(--text-teal); }
  .shipping { position: absolute; left: 390px; top: 426px; font-family: 'Questrial', sans-serif; font-size: 21px; color: var(--text-brown); }
  .product-photo {
    position: absolute; left: 856px; top: 138px; width: 270px; height: 322px;
    background: linear-gradient(90deg, #1c1c1c 0%, #2a2a2a 38%, #f4f4f2 46%, #ffffff 70%, #e6e6e6 100%);
    border-radius: 6px;
  }
</style>
</head>
<body>
<div class="banner">
  <svg class="top-band" viewBox="0 0 1200 82" aria-hidden="true">
    <rect width="1200" height="82" fill="var(--brown)"/>
    <polygon points="0,0 130,0 250,82 0,82" fill="var(--teal)"/>
    <polygon points="130,0 180,0 300,82 250,82" fill="var(--white)"/>
    <polygon points="505,0 535,0 520,82 490,82" fill="var(--white)"/>
    <polygon points="535,0 615,0 640,82 520,82" fill="var(--teal)"/>
    <polygon points="615,0 665,0 690,82 640,82" fill="var(--white)"/>
    <polygon points="900,0 1000,0 935,82 830,82" fill="var(--teal)"/>
    <polygon points="1000,0 1060,0 990,82 935,82" fill="var(--white)"/>
    <polygon points="1060,0 1200,0 1200,82 990,82" fill="var(--brown)"/>
  </svg>

  <svg class="badge" viewBox="0 0 326 326" aria-hidden="true">
    <circle cx="163" cy="163" r="163" fill="var(--brown)"/>
    <circle cx="163" cy="163" r="150" fill="var(--teal)"/>
    <circle cx="163" cy="163" r="126" fill="var(--ivory)"/>
    <circle cx="163" cy="163" r="104" fill="var(--teal)"/>
    <g stroke="var(--ivory)" stroke-width="2">
      <line x1="103" y1="95" x2="145" y2="95"/>
      <line x1="181" y1="95" x2="223" y2="95"/>
      <line x1="103" y1="234" x2="145" y2="234"/>
      <line x1="181" y1="234" x2="223" y2="234"/>
    </g>
    <rect x="150" y="90" width="26" height="9" rx="4" fill="var(--ivory)" role="img" aria-label="Small moustache ornament"/>
    <rect x="150" y="229" width="26" height="9" rx="4" fill="var(--ivory)" role="img" aria-label="Small moustache ornament"/>
  </svg>
  <div class="badge-title">
    <span class="small">Father's Day</span>
    <span class="large">Deal!</span>
  </div>

  <p class="headline">Who needs another tie?</p>
  <p class="lede">Show dad how much you love him with a beautiful candle!</p>
  <p class="save">Save</p>
  <p class="discount">30<sup>%</sup></p>
  <p class="scope">Off ALL Candles</p>
  <p class="shipping">Free Shipping when you order $75 or more!</p>

  <div class="product-photo" role="img" aria-label="Photo of the Cedar Hollow Candle starlit jar candle beside its black gift tube and lid"></div>
  <div class="bottom-band"></div>
</div>
</body>
</html>
```